Kelmora Business Card

We want a logo that connects with the target consumer who are Retailers in the giftware/wholesale/ecommerce space. We will be constantly changing product lines and industry. We are after a logo that can communicate the meaning of "Kelmora"which means Divine/spiritual/light. The company name and owners are of Indian nationals and want to bring the positivity/growth in the design as a subtle message.
Have attached a logo that we think captures the essence of the word "Kelmora" which is light/glow/divine.

Target Market(s)

Adults based in Australia english speaking aged 20 - 60 years that are in the retail business.

Industry/Entity Type

Business

Font styles to use
Serif
Sans Serif
Decorative
Script

Requirements
Must have
• Logo in form of "D" or "Kelmora" or "Kelmora Pty Ltd"
Nice to have
• I have attached a sample of letter D used as logo. Its shows the glowing sun which is representative/symbolic presentation of word "Kelmora"

```html
<!DOCTYPE html>
<html lang="en">
<head>
<meta charset="utf-8">
<title>Kelmora Business Card</title>
<link rel="stylesheet" href="https://fonts.googleapis.com/css2?family=Montserrat:wght@400;700&family=Open+Sans:wght@400;600&display=swap">
<style>
  :root {
    --canvas: #eeeeef;
    --card: #ffffff;
    --navy: #1f2d5c;
    --ink: #4a4f5c;
    --muted: #7a7f8a;
    --rule: #c9ccd2;
    --orange: #f5a11f;
    --photo: #9a9ca1;
  }
  * { box-sizing: border-box; margin: 0; padding: 0; }
  html, body { width: 1200px; height: 800px; overflow: hidden; }
  body {
    background: var(--canvas);
    font-family: "Open Sans", Arial, sans-serif;
    position: relative;
  }
  .card {
    position: absolute;
    top: 257px;
    width: 500px;
    height: 286px;
    background: var(--card);
    box-shadow: 0 10px 28px rgba(0,0,0,0.10), 0 2px 6px rgba(0,0,0,0.06);
  }
  .card--front { left: 70px; }
  .card--back { left: 630px; }

  .brand { display: flex; align-items: center; gap: 10px; }
  .brand__square { width: 34px; height: 34px; background: var(--orange); flex: none; }
  .brand__name {
    font-family: "Montserrat", Arial, sans-serif;
    font-weight: 700;
    color: var(--navy);
    letter-spacing: 0.5px;
    line-height: 1.05;
  }

  .card--front .brand { position: absolute; left: 36px; top: 118px; }
  .card--front .brand__name { font-size: 20px; }

  .photo {
    position: absolute;
    right: 36px;
    top: 30px;
    width: 56px;
    height: 46px;
    background: var(--photo);
    border: 3px solid #e2e3e6;
  }
  .contact {
    position: absolute;
    left: 230px;
    right: 36px;
    top: 100px;
    color: var(--ink);
    font-size: 10.5px;
  }
  .contact__name { font-size: 15px; color: var(--ink); letter-spacing: 0.3px; }
  .contact__name strong { font-weight: 600; }
  .contact__line { padding: 7px 0; border-top: 1px solid var(--rule); }
  .contact__line:first-child { border-top: none; padding-top: 0; }
  .contact__email { color: var(--navy); }
  .contact__web {
    position: absolute;
    right: 36px;
    bottom: 30px;
    font-size: 10px;
    color: var(--muted);
  }

  .card--back .centre {
    position: absolute;
    inset: 0;
    display: flex;
    flex-direction: column;
    align-items: center;
    justify-content: center;
    gap: 10px;
  }
  .card--back .brand__name { font-size: 22px; }
  .card--back .brand__square { width: 30px; height: 30px; }
  .back__web { font-size: 10.5px; color: var(--navy); }
</style>
</head>
<body>
  <section class="card card--front">
    <div class="brand">
      <span class="brand__square"></span>
      <span class="brand__name">KELMORA<br>PTY LTD</span>
    </div>
    <div class="photo" role="img" aria-label="Portrait photo of the card holder"></div>
    <div class="contact">
      <p class="contact__line contact__name">Arlo Brennan | <strong>Your profession</strong></p>
      <p class="contact__line">Your Address | STATE TOWN COUNTRY</p>
      <p class="contact__line">Phone 555-210-384</p>
      <p class="contact__line contact__email">arlo@kelmora.net</p>
    </div>
    <p class="contact__web">www.kelmora.net</p>
  </section>

  <section class="card card--back">
    <div class="centre">
      <div class="brand">
        <span class="brand__square"></span>
        <span class="brand__name">KELMORA PTY LTD</span>
      </div>
      <p class="back__web">www.kelmoraonline.net</p>
    </div>
  </section>
</body>
</html>
```